Brochure for Specialist Divorce Support

1. I want an A4 three fold brochure or DL to promote my business and services.
My market are people going through divorce and are usually feeling very overwhelmed and therefore not functioning very well - both men and women, age early forties,
2. Colours – variety of blues and lime greens but you choose if you need a contrast e.g. orange
3. Images – happy single families
4. Theme - could you make it around water please - soothing
5. Logos – HWN &; HWT (I will attach)
6. I have a lot of content so maybe not too busy but still professional feel +
warm and reassuring
7. I'm attaching -

- a draft brochure I put together using a Microsoft template
- a word document with extra details
- plus two logos to do with my qualifications
- and some images for you to choose from

7. I want to use this as a template for some other brochures -> more work for
the winner.

Target Market(s)

Men and women usually in their early forties with primary school aged children i.e 5 to 12 years old.
They are going through a divorce and very upset, Maybe losing contact with their children and their way of life as they know it is disappearing. They are in turmoil and not functioning as well as they usually do.

Industry/Entity Type

Business

Font styles to use
Sans Serif

Colors
34a7d7
abd037
3277b5

Requirements
Must have
• I want the brochure to be three folds with the center the full A4
• Could you make the theme around water please.
• I will upload some photos for you to use if you want,

```html
<!DOCTYPE html>
<html lang="en">
<head>
<meta charset="utf-8">
<title>Specialist Divorce Support – Brochure</title>
<link rel="stylesheet" href="https://fonts.googleapis.com/css2?family=Roboto+Condensed:ital,wght@0,300;0,400;0,700;1,700&family=Roboto:ital,wght@0,400;0,700;1,400&display=swap">
<style>
:root{
  --bg:#d6d8d7;
  --paper:#ffffff;
  --navy:#2d5aa3;
  --blue:#2e5da6;
  --sky:#1ba3dc;
  --lime:#c3d12f;
  --lime-dark:#a9bb1f;
  --ink:#2b2b2b;
  --orange:#e0922a;
  --cream:#fdf6c0;
}
*{box-sizing:border-box;margin:0;padding:0}
html,body{width:960px;height:1200px;overflow:hidden;background:var(--bg)}
body{position:relative;font-family:'Roboto',Arial,sans-serif;color:var(--ink)}
.sheet{position:absolute;left:124px;width:713px;height:504px;background:var(--paper);overflow:hidden}
.sheet-outside{top:84px}
.sheet-inside{top:612px}
.panel{position:absolute;top:0;width:238px;height:504px}
.p1{left:0}.p2{left:238px}.p3{left:476px;width:237px}
.photo{position:absolute;display:block}
.blue{background:var(--blue);color:#fff}
.small-list{list-style:none;font-size:7px;line-height:8.6px}
.small-list li{position:relative;padding-left:12px;margin-bottom:5px}
.small-list li::before{content:"";position:absolute;left:1px;top:3px;width:3px;height:3px;border-radius:50%;background:currentColor}
.cond{font-family:'Roboto Condensed','Arial Narrow',sans-serif}
.qmark{position:absolute;font-family:'Roboto Condensed',sans-serif;font-weight:700;color:var(--lime-dark);line-height:1}

/* outside left */
.callout{position:absolute;left:0;top:130px;width:238px;height:107px;background:var(--lime)}
.callout-tail{position:absolute;left:112px;top:236px}
.callout-text{position:absolute;left:55px;top:8px;width:172px;font-size:9.8px;line-height:14px;font-weight:700;color:#2e3312}
.help-title{position:absolute;left:18px;top:256px;font-size:7.4px;font-weight:700}
.help-list{position:absolute;left:18px;top:270px;width:200px}
.pace-quote{position:absolute;left:43px;top:467px;width:180px;font-size:10px;line-height:12.4px;font-weight:700;color:var(--navy)}

/* testimonial */
.testimonial{position:absolute;left:20px;top:50px;width:198px;height:261px;border:1px solid var(--sky);border-radius:8px;padding:20px 12px 0;text-align:center}
.testimonial-label{position:absolute;left:55px;top:-8px;width:86px;height:15px;background:var(--sky);font-size:11px;font-weight:700;line-height:15px;text-align:center;letter-spacing:.2px}
.testimonial p{font-style:italic;font-size:8.8px;line-height:12.2px;margin-bottom:11px}
.client-name{font-size:8.4px;font-weight:700;margin-top:2px}
.client-place{font-size:6.6px}
.contact{position:absolute;left:28px;top:378px;width:182px;text-align:center;font-size:7.6px;line-height:10px}
.contact strong{display:block;margin-bottom:11px}

/* cover */
.cover-fade{position:absolute;left:0;top:0;width:237px;height:504px;background:linear-gradient(180deg,#b7a983 0%,#c9b898 40%,#f6eec9 62%,var(--cream) 100%)}
.cover-label{position:absolute;left:28px;top:296px;font-size:22px;font-weight:700;color:var(--navy);letter-spacing:.2px}
.cover-title{position:absolute;left:27px;top:319px;font-size:50px;font-weight:300;line-height:40px;color:#2c2c2c;transform:scaleY(1.15);transform-origin:0 0;white-space:nowrap}
.cover-lede{position:absolute;left:28px;top:434px;width:200px;font-size:8.6px;line-height:11.4px;font-style:italic;font-weight:700;color:#2e3312}
.cover-bar{position:absolute;left:28px;top:488px;width:209px;height:16px;background:var(--orange)}

/* inside */
.tailored{position:absolute;left:20px;top:20px;line-height:17px}
.tailored .t1{font-size:17px;font-weight:700;color:var(--lime-dark);display:block}
.tailored .t2{font-size:20px;font-weight:300;color:var(--navy);display:block;transform:scaleY(1.25);transform-origin:0 0;white-space:nowrap}
.services-title{position:absolute;left:20px;top:70px;font-size:7.4px;font-weight:700}
.services-list{position:absolute;left:20px;top:85px;width:210px}
.stages{position:absolute;left:10px;top:22px;width:222px;font-size:7px;line-height:8.6px}
.stages .intro{margin-bottom:6px}
.stage-head{font-weight:700;padding-left:13px;position:relative;margin-bottom:5px}
.stage-head span{position:absolute;left:0}
.stages p.body{padding-left:13px;margin-bottom:5px}
.stages .small-list{padding-left:13px}
.right-col{position:absolute;left:16px;top:22px;width:200px;font-size:7px;line-height:8.6px}
.right-col .small-list li{margin-bottom:4px}
.note{font-style:italic;margin:-2px 0 4px 12px}
.end-line{font-weight:700;margin-top:4px}
.strip-quote{position:absolute;left:238px;top:341px;width:158px;height:163px;background:var(--lime)}
.strip-quote p{position:absolute;left:33px;top:30px;width:122px;font-size:9.8px;line-height:15px;font-weight:700;color:#2e3312}
</style>
</head>
<body>

<section class="sheet sheet-outside">
  <div class="panel p1">
    <div class="photo" role="img" aria-label="Photo of a father hugging his two children on a beach" style="left:0;top:0;width:238px;height:130px;background:linear-gradient(180deg,#8a8576 0%,#a39c8c 55%,#b9ad94 100%)"></div>
    <div class="callout">
      <span class="qmark" style="left:18px;top:-6px;font-size:54px">“</span>
      <p class="callout-text cond">Often family and friends can try to influence decisions based on what they see as best, so you can feel under an enormous pressure to keep them happy. Coaching offers an objective and neutral sounding board there just for you.</p>
      <span class="qmark" style="left:154px;top:74px;font-size:34px">”</span>
    </div>
    <svg class="callout-tail" width="20" height="16" viewBox="0 0 20 16"><polygon points="0,0 14,0 2,16" fill="#c3d12f"/></svg>
    <p class="help-title">Coaching can help you:</p>
    <ul class="small-list help-list">
      <li>Save money by being a more collected and credible client in the legal process</li>
      <li>Stay in control and focus on what's important for you and your family to avoid angry, emotional hijacks</li>
      <li>Feel more empowered by being organised and prepared for what's ahead and develop a plan of action</li>
      <li>Identify your next steps re: legal, financial, children's issues plus your self-care</li>
      <li>Develop a draft parenting plan to anticipate and address possible issues pertinent to your family</li>
      <li>Consider areas of possible conflict and explore techniques to reduce confrontation</li>
      <li>Find your voice and be more confident in your skills to take control of your divorce and do it your way</li>
      <li>Let go of what was … and create what is possible during your divorce journey and afterwards.</li>
    </ul>
    <span class="qmark" style="left:10px;top:446px;font-size:60px;color:#e8e8e8">“</span>
    <p class="pace-quote cond">“Everyone is different and move through these stages at their own pace”</p>
    <span class="qmark" style="left:174px;top:478px;font-size:34px;color:#e8e8e8">”</span>
  </div>

  <div class="panel p2 blue">
    <div class="testimonial">
      <div class="testimonial-label cond">TESTIMONIAL</div>
      <p>"After many cups of coffee and long hours of listening to me, my very good friend suggested I speak to Melissa, a divorce coach. I was a bit skeptical, especially when a phone session was suggested.</p>
      <p>From my first phone session I felt empowered. It gave me a sense of direction, assisted me to set realistic goals and action plans. Most importantly it aided my self esteem.</p>
      <p>Divorce is overwhelming. Talking to a caring professional like Helena helped me acknowledge my priorities and a way to achieve them. Thank you Helena. "</p>
      <div class="client-name">Marisa</div>
      <div class="client-place">Ccccccc, Smmmmm. AAA</div>
    </div>
    <div class="contact">
      <strong>Coaching works well over the phone, allowing for flexibility of time and place - evening appointments available.</strong>
      Full details are on:<br>
      --------------------------------<br>
      or email:<br>
      Helena@.................................
    </div>
  </div>

  <div class="panel p3">
    <div class="cover-fade" role="img" aria-label="Photo of a smiling mother embracing her daughter outdoors"></div>
    <h2 class="cover-label cond">SPECIALIST</h2>
    <h1 class="cover-title cond">DIVORCE<br>SUPPORT</h1>
    <p class="cover-lede">Together we will identify your goals, set priorities and develop a plan for tomorrow … moving you through the pain of divorce to regain confidence and start anew.</p>
    <div class="cover-bar"></div>
  </div>
</section>

<section class="sheet sheet-inside">
  <div class="panel p1">
    <h2 class="tailored cond"><span class="t1">TAILORED</span><span class="t2">DIVORCE SUPPORT</span></h2>
    <p class="services-title">My services:</p>
    <ul class="small-list services-list">
      <li>Specialist divorce support to suit your needs</li>
      <li>Pre-mediation coaching helping you prepare and achieve more positive outcomes to avoid going to court</li>
      <li>Collaborative law coaching to increase crucial skills so you can participate more constructively in negotiations</li>
      <li>Delivery of HWN Conflict Style Profile giving you real feedback on the constructive and destructive behaviours you choose during conflict situations to facilitate more productive discussions</li>
      <li>Corporate Conflict Management Training</li>
    </ul>
    <div class="photo" role="img" aria-label="Photo of a father and son playing football on a sunny lawn" style="left:0;top:190px;width:238px;height:314px;background:linear-gradient(180deg,#ffffff 0%,#e4eed8 18%,#a9c987 50%,#5f9a3a 100%)"></div>
  </div>

  <div class="panel p2 blue" style="height:341px">
    <div class="stages">
      <p class="intro">You will go through distinct stages:</p>
      <p class="stage-head"><span>1.</span>The Preparation Stage – maybe entail one or two coaching sessions</p>
      <p class="body">Anticipating all the unknowns and preparing before you see a Family Law Solicitor can save a lot of your solicitor's time and therefore money. The clearer you are on what you want to achieve throughout the process, the more specific legal advice you will receive.</p>
      <p class="stage-head"><span>2.</span>The Business Side of Divorce – maybe two to four coaching sessions</p>
      <p class="body">Divorce involves multiple areas of change, intensity of emotions, life changing decisions, loss of family structure and often a sense of isolation not experienced before. Necessary</p>
      <p class="body">The emotional overwhelm associated with relationship breakdown and the associated loss of 24/7 contact with children can impact even the most together person's ability to make well considered decisions.</p>
      <p class="body">Together, we will process emotions constructively and clarify decisions to be made... for you to be better able to communicate these in negotiations as well as set new boundaries.</p>
      <p class="body" style="font-weight:700">Where necessary we can work on skills you will need for successful outcomes with property settlements and parenting orders e.g.</p>
      <ul class="small-list">
        <li>conflict resolution skills plus specific verbal &amp; written communication skills important for more neutral emails and messages</li>
        <li>having difficult conversations</li>
      </ul>
    </div>
  </div>

  <div class="panel p3" style="height:341px">
    <div class="right-col">
      <ul class="small-list">
        <li>preparing before attending joint conferences or mediation</li>
        <li>managing anger</li>
        <li>supporting your children to also navigate changed family structures</li>
        <li>strategies for you to start healing and become whole again</li>
        <li>drafting a parenting plan to anticipate &amp; address possible parenting issues, leading to more positive and successful co-parenting in the long term.</li>
      </ul>
      <p class="note">This is in everyone's interests... especially your children's.</p>
      <ul class="small-list">
        <li>grieving losses ... even if you are the one who made the decision to leave</li>
        <li>look at possible stress strategies to sustain your energy levels, important for you to make good considered decisions</li>
      </ul>
      <p class="stage-head" style="padding-left:13px"><span>3.</span>The Moving On Stage – one or two coaching sessions</p>
      <p style="padding-left:13px;margin-bottom:4px">Dealing with endings and focusing on the future:</p>
      <ul class="small-list" style="padding-left:13px">
        <li>changing your "self" image and building self worth</li>
        <li>transitioning from married life to being single again</li>
        <li>address barriers preventing you form moving forward</li>
        <li>setting realistic goals to help transition to your new life more effectively</li>
      </ul>
      <p class="end-line">Everyone is different and moves through the stages at their own pace.</p>
    </div>
  </div>

  <div class="photo" role="img" aria-label="Photo of a mother playing with her son and daughter on the grass" style="left:396px;top:341px;width:317px;height:163px;background:linear-gradient(160deg,#a9c46a 0%,#8fb04c 40%,#6c8f33 75%,#54722a 100%)"></div>
  <div class="strip-quote">
    <span class="qmark" style="left:8px;top:12px;font-size:54px">“</span>
    <p class="cond">Every divorce is different and families going forward will be different. I try to get my client to see or find ways they can co-parent as opposed to being one of two single parents.</p>
    <span class="qmark" style="left:112px;top:132px;font-size:34px">”</span>
  </div>
</section>

</body>
</html>
```